Elegant Black Candle Label Design!

I need a 2.375" tall by 3.0" wide candle label design. I'm looking for simple and elegant. Black label with silver leaf border and lettering. Label needs to have the following information on it: Fern Hollow Candle Co. as the company name, scent name in the middle and in smaller font, it needs to say Made in USA, All Natural, 8oz. Attached photos are for inspiration.

Target Market(s)

People looking for high end, all natural candle fragrances

Industry/Entity Type

Candle-Spa

Colors

Designer to choose only greyscale colors for use in the design.

Requirements
Must have
• Company Name, Scent (ability to change scent names), All Natural, Made in USA, 8oz
Nice to have
• Black background, silver leaf border and silver leaf font. Elegant fonts maybe slightly cursive

```html
<!DOCTYPE html>
<html lang="en">
<head>
<meta charset="UTF-8">
<title>Fern Hollow Candle Co. — Candle Label</title>
<link href="https://fonts.googleapis.com/css2?family=Cormorant+Garamond:wght@400;500&display=swap" rel="stylesheet">
<style>
  :root {
    --page-bg: #e6e6e6;
    --label-black: #111111;
    --silver: #c4c4c4;
    --silver-soft: #a9a9a9;
  }
  * { margin: 0; padding: 0; box-sizing: border-box; }
  html, body {
    width: 1200px;
    height: 1200px;
    overflow: hidden;
    background: var(--page-bg);
  }
  .label {
    position: absolute;
    left: 100px;
    top: 204px;
    width: 1000px;
    height: 792px;
    background: var(--label-black);
    font-family: "Cormorant Garamond", serif;
    color: var(--silver);
  }
  .brand-name {
    position: absolute;
    left: 0;
    right: 0;
    top: 320px;
    text-align: center;
    font-size: 74px;
    font-weight: 500;
    letter-spacing: 1px;
    color: var(--silver);
  }
  .scent-list {
    position: absolute;
    left: 184px;
    top: 560px;
    list-style: none;
    font-size: 42px;
    font-weight: 400;
    line-height: 48px;
    color: var(--silver);
  }
  .rule {
    position: absolute;
    background: var(--silver-soft);
  }
  .rule-main-vertical { left: 417px; top: 555px; width: 2px; height: 167px; }
  .rule-horizontal    { left: 444px; top: 632px; width: 351px; height: 2px; }
  .rule-small-vertical{ left: 558px; top: 648px; width: 2px; height: 74px; }
  .info {
    position: absolute;
    font-size: 42px;
    font-weight: 400;
    white-space: nowrap;
    color: var(--silver);
  }
  .info-origin  { left: 484px; top: 560px; }
  .info-weight  { left: 446px; top: 654px; }
  .info-natural { left: 584px; top: 654px; }
</style>
</head>
<body>
  <main class="label">
    <h1 class="brand-name">Fern Hollow Candle Co.</h1>

    <ul class="scent-list">
      <li>Cyprus</li>
      <li>Plum</li>
      <li>Juniper</li>
    </ul>

    <span class="rule rule-main-vertical"></span>
    <span class="rule rule-horizontal"></span>
    <span class="rule rule-small-vertical"></span>

    <p class="info info-origin">Made in USA</p>
    <p class="info info-weight">8 oz.</p>
    <p class="info info-natural">All natural</p>
  </main>
</body>
</html>
```